" é uma empresa produtora de polpas de frutas congeladas, sumos naturais, e gelados artesanais. comercialisamos os produtos para pessoas individuais , lojas, restaurants e eventos. funcianamento: a materia prima (fruta) chega a fabrica, e é processeda segungo um protocolo definido pelas normas de saude e higiene. posterioremente é embalado e armazenado. os pedidos dos clientes chegam por telefone ou whatsaap e nós procedemos de acordo. fazemos entregas ou o cliente vem a loja. em junho sera aberta a loja/restaurante/gelataria fisica. todos os products são processados por nós. usamos produtos de qualidade, sem corantes e sem conservantes artificiais. "

```html
<!DOCTYPE html>
<html lang="pt">
<head>
<meta charset="utf-8">
<title>Frutos do Kwanza – Cartões de Visita</title>
<link rel="stylesheet" href="https://fonts.googleapis.com/css2?family=Montserrat:wght@400;600;700&display=swap">
<style>
  :root{
    --bg:#2b2b2d;
    --red-deep:#5e0710;
    --red-main:#9c1420;
    --red-bright:#c4222c;
    --gold:#f2b51c;
    --gold-dark:#d58f0c;
    --white:#ffffff;
    --photo-a:#7a0c15;
    --photo-b:#3e0308;
  }
  *{box-sizing:border-box;margin:0;padding:0}
  html,body{width:1200px;height:1200px;overflow:hidden}
  body{background:var(--bg);font-family:"Montserrat",sans-serif;position:relative}

  .card{
    position:absolute;border-radius:22px;overflow:hidden;
    background:radial-gradient(ellipse at 60% 30%,var(--red-bright) 0%,var(--red-main) 45%,var(--red-deep) 100%);
    box-shadow:0 18px 40px rgba(0,0,0,.5);
  }
  .card-front{left:60px;top:250px;width:400px;height:700px}
  .card-back{left:520px;top:423px;width:620px;height:354px}

  .swirl{position:absolute;inset:0;width:100%;height:100%}

  .edge-tab{position:absolute;background:linear-gradient(90deg,var(--gold-dark),var(--gold))}
  .card-front .edge-tab{left:0;top:300px;width:14px;height:290px;border-radius:0 8px 8px 0}
  .card-back .edge-tab{right:0;top:70px;width:14px;height:230px;border-radius:8px 0 0 8px}

  .brand{
    position:absolute;display:flex;align-items:center;gap:10px;
    font-family:"Montserrat",sans-serif;font-weight:700;color:var(--gold);white-space:nowrap;
  }
  .brand-dot{width:14px;height:14px;border-radius:50%;background:var(--gold);flex:none}

  .card-front .brand{left:0;right:0;top:130px;justify-content:center;font-size:30px}
  .card-back .brand{left:48px;top:160px;font-size:22px}

  .photo-baobab{
    position:absolute;left:0;right:0;bottom:0;height:400px;
    background:linear-gradient(180deg,rgba(62,3,8,0) 0%,var(--photo-a) 35%,var(--photo-b) 100%);
  }
  .slogan{
    position:absolute;left:40px;right:30px;bottom:150px;
    font-family:"Montserrat",sans-serif;font-weight:600;font-size:30px;color:var(--gold);
  }

  .contact{position:absolute;right:78px;top:78px;text-align:right;color:var(--white)}
  .contact-name{font-weight:700;font-size:24px}
  .contact-role{font-size:12px;margin-top:2px;margin-bottom:20px}
  .contact-lines{list-style:none;font-size:10.5px;line-height:2.05}
  .contact-icons{position:absolute;right:38px;top:148px;display:flex;flex-direction:column;gap:11px}
  .icon{width:17px;height:17px;border-radius:50%;background:var(--white);display:flex;align-items:center;justify-content:center}
  .icon svg{width:10px;height:10px}
</style>
</head>
<body>

<section class="card card-front">
  <svg class="swirl" viewBox="0 0 400 700" preserveAspectRatio="none" aria-hidden="true">
    <path d="M0 120 C90 160 60 300 0 330 Z" fill="#6d0a13" opacity=".8"/>
    <path d="M0 240 C120 200 160 330 400 300 L400 360 C200 380 120 280 0 320 Z" fill="#7e0d17" opacity=".6"/>
  </svg>
  <div class="photo-baobab" role="img" aria-label="Fotografia de um embondeiro (baobá) em tons de vermelho"></div>
  <div class="edge-tab"></div>
  <div class="brand"><span class="brand-dot"></span>Frutos do Kwanza</div>
  <div class="slogan">Fruta de Verdade</div>
</section>

<section class="card card-back">
  <svg class="swirl" viewBox="0 0 620 354" preserveAspectRatio="none" aria-hidden="true">
    <path d="M0 0 L170 0 C120 90 200 200 90 354 L0 354 Z" fill="#6d0a13" opacity=".7"/>
    <path d="M0 260 C150 200 260 330 420 354 L0 354 Z" fill="#7e0d17" opacity=".55"/>
  </svg>
  <div class="edge-tab"></div>
  <div class="brand"><span class="brand-dot"></span>Frutos do Kwanza</div>
  <div class="contact">
    <div class="contact-name">Nome Completo</div>
    <div class="contact-role">Cargo</div>
    <ul class="contact-lines">
      <li>+244 923 000 111 · Geral</li>
      <li>+244 912 000 222 · Encomendas</li>
      <li>Rua das Acácias, 45 – Luanda</li>
      <li>geral@frutoskwanza.ao</li>
      <li>www.frutoskwanza.ao</li>
    </ul>
  </div>
  <div class="contact-icons">
    <span class="icon"><svg viewBox="0 0 10 10"><path d="M2 1 L4 1 L4.6 3 L3.5 3.8 C4 5 5 6 6.2 6.5 L7 5.4 L9 6 L9 8 C5 8.5 1.5 5 2 1 Z" fill="#9c1420"/></svg></span>
    <span class="icon"><svg viewBox="0 0 10 10"><circle cx="5" cy="5" r="3" fill="#9c1420"/></svg></span>
    <span class="icon"><svg viewBox="0 0 10 10"><path d="M5 1 C3 1 2 2.5 2 4 C2 6 5 9 5 9 C5 9 8 6 8 4 C8 2.5 7 1 5 1 Z" fill="#9c1420"/></svg></span>
    <span class="icon"><svg viewBox="0 0 10 10"><rect x="1.5" y="2.5" width="7" height="5" fill="none" stroke="#9c1420" stroke-width="1.2"/><path d="M1.5 2.5 L5 5.5 L8.5 2.5" fill="none" stroke="#9c1420" stroke-width="1.2"/></svg></span>
    <span class="icon"><svg viewBox="0 0 10 10"><circle cx="5" cy="5" r="3.5" fill="none" stroke="#9c1420" stroke-width="1.2"/><path d="M1.5 5 H8.5 M5 1.5 V8.5" stroke="#9c1420" stroke-width="1"/></svg></span>
  </div>
</section>

</body>
</html>
```